High end wine label at Austrian Winery

We are a traditional winery in Austria in region Burgenland. We are looking for a relaunch of our current wine label for our [solstice] series. It's a high end wine series at an upper price range. At the moment we have just two kinds of the label, one white one for the white wines and one black one for the red wines. This is a series of wine, white, red, sweet, sparkling and a top wine categories. So we need the same label, but in 4 different ways to distinguish the wines plus the sparkling. Maybe in color, patterns, ... or something else. The label should be very simple, including our new logo. It's also possible to make one label but we can splitting two parts of the label. The size of the label does not matter, need not be the same as now. It's a bit higher than a normal bottle. Additionally we need a back label with wine description and the wine dates on it.

Target Market(s)

private consumers and restaurants, no retailers

Colors

Designer to choose colors to be used in the design.

Requirements
Must have
• simple label with 4 different categories (red, white, sweet, top) plus Frizzante label, new logo integrated, high end label. Just logo, grape variety and [solstice] as text on the front label as text
Nice to have
• It's just good, if there'sa possibility to have different colors of each grape variety (about 10 different), but all the same style. top Wines should have an extraordinary design, but familiar with the others
Should not have
• no cheap look

```html
<!DOCTYPE html>
<html lang="en">
<head>
<meta charset="utf-8">
<title>Halden – Wine Label Series</title>
<link href="https://fonts.googleapis.com/css2?family=Montserrat:wght@500;600&family=Raleway:wght@300;400&family=Great+Vibes&display=swap" rel="stylesheet">
<style>
  :root{
    --bg:#e6e6e6;
    --navy:#323a4b;
    --slate:#728c99;
    --slate-light:#8ea3ae;
    --ink-black:#1e1d21;
    --white:#ffffff;
    --grey-dark:#3f3f3f;
    --grey-mid:#8c8c8c;
    --grey-light:#a9a9a9;
  }
  html,body{margin:0;padding:0;overflow:hidden;}
  body{width:1200px;height:1200px;background:var(--bg);position:relative;}

  .label{
    position:absolute;
    width:calc(428px*var(--k));
    height:calc(532px*var(--k));
    color:var(--ink);
  }
  .label--large{--k:1;}
  .label--small{--k:0.43;}

  .label__shape{position:absolute;inset:0;width:100%;height:100%;overflow:visible;}
  .label__halo{fill:none;stroke:var(--halo);stroke-width:22;stroke-linejoin:round;}
  .label__body{fill:var(--fill);stroke:var(--edge);stroke-width:10;stroke-linejoin:round;}

  .label__mark{
    position:absolute;
    left:calc(134px*var(--k));top:calc(20px*var(--k));
    width:calc(160px*var(--k));height:calc(160px*var(--k));
    border:calc(4px*var(--k)) solid var(--edge);
    border-radius:50%;box-sizing:border-box;
    display:flex;align-items:center;justify-content:center;
    font-family:"Montserrat",sans-serif;font-weight:600;
    font-size:calc(22px*var(--k));letter-spacing:.2em;
    color:var(--ink);
  }
  .label__brand{
    position:absolute;left:0;right:0;top:calc(222px*var(--k));
    text-align:center;
    font-family:"Montserrat",sans-serif;font-weight:600;
    font-size:calc(54px*var(--k));letter-spacing:.17em;
    text-indent:.17em;line-height:1;color:var(--ink);
  }
  .label__since{
    position:absolute;left:0;right:0;top:calc(286px*var(--k));
    text-align:center;
    font-family:"Montserrat",sans-serif;font-weight:600;
    font-size:calc(19px*var(--k));letter-spacing:.24em;
    line-height:1;color:var(--sub);
  }
  .label__variety{
    position:absolute;left:0;right:0;top:calc(400px*var(--k));
    text-align:center;
    font-family:"Great Vibes",cursive;
    font-size:calc(58px*var(--k));line-height:1;color:var(--ink);
  }
  .label__variety--long{font-size:calc(40px*var(--k));top:calc(414px*var(--k));}
  .label__rule{
    position:absolute;left:calc(56px*var(--k));right:calc(56px*var(--k));
    top:calc(474px*var(--k));height:calc(2px*var(--k));
    background:var(--sub);opacity:.8;
  }
  .label__series{
    position:absolute;left:0;right:0;top:calc(479px*var(--k));
    text-align:center;
    font-family:"Raleway",sans-serif;font-weight:300;
    font-size:calc(18px*var(--k));line-height:1;color:var(--ink);
  }

  .label__heading{
    position:absolute;left:0;right:0;top:calc(118px*var(--k));
    text-align:center;
    font-family:"Raleway",sans-serif;font-weight:400;
    font-size:calc(26px*var(--k));line-height:1;color:var(--ink);
  }
  .label__ingredients{
    position:absolute;left:calc(102px*var(--k));top:calc(150px*var(--k));
    width:calc(240px*var(--k));margin:0;
    font-family:"Raleway",sans-serif;font-weight:300;
    font-size:calc(25px*var(--k));line-height:1.2;color:var(--sub);
  }
  .label__fact{
    position:absolute;top:calc(420px*var(--k));
    font-family:"Raleway",sans-serif;line-height:1.1;
  }
  .label__fact--net{left:calc(64px*var(--k));}
  .label__fact--maker{left:calc(276px*var(--k));}
  .label__fact-key{display:block;font-weight:400;font-size:calc(21px*var(--k));color:var(--ink);}
  .label__fact-value{display:block;font-weight:300;font-size:calc(27px*var(--k));color:var(--sub);}

  .label--white{--fill:var(--white);--edge:var(--slate);--halo:var(--white);--ink:var(--navy);--sub:var(--slate);}
  .label--white .label__heading,.label--white .label__fact-key{color:var(--slate);}
  .label--red{--fill:var(--navy);--edge:var(--slate);--halo:var(--slate-light);--ink:var(--white);--sub:var(--slate);}
  .label--red.label--back{--sub:#e3e8ec;}
  .label--sweet{--fill:var(--slate);--edge:var(--navy);--halo:var(--slate-light);--ink:var(--navy);--sub:var(--white);}
  .label--sweet.label--back{--ink:var(--white);--sub:#e8eef1;}
  .label--top{--fill:var(--ink-black);--edge:var(--white);--halo:var(--ink-black);--ink:var(--white);--sub:var(--white);}
  .label--sparkle{--fill:url(#sparkleFill);--edge:var(--grey-light);--halo:var(--grey-mid);--ink:var(--grey-dark);--sub:#b4b4b4;}
  .label--sparkle.label--back{--sub:var(--grey-dark);}
</style>
</head>
<body>

<svg width="0" height="0" style="position:absolute" aria-hidden="true">
  <defs>
    <path id="labelOutline" d="M0,105 C120,40 180,0 267,0 C354,0 414,40 535,105 C505,300 505,450 535,600 C400,660 135,660 0,600 C30,450 30,250 0,105 Z"/>
    <linearGradient id="sparkleFill" x1="0" y1="0" x2="0" y2="1">
      <stop offset="0" stop-color="#7d7d7d"/>
      <stop offset=".45" stop-color="#9a9a9a"/>
      <stop offset="1" stop-color="#8a8a8a"/>
    </linearGradient>
  </defs>
</svg>

<!-- White: front -->
<div class="label label--large label--white label--front" style="left:156px;top:64px">
  <svg class="label__shape" viewBox="0 0 535 665" preserveAspectRatio="none"><use href="#labelOutline" class="label__halo"/><use href="#labelOutline" class="label__body"/></svg>
  <div class="label__mark">HALDEN</div>
  <div class="label__brand">HALDEN</div>
  <div class="label__since">.WINE SINCE 1931</div>
  <div class="label__variety">White</div>
  <div class="label__rule"></div>
  <div class="label__series">[solstice]</div>
</div>
<!-- White: back -->
<div class="label label--large label--white label--back" style="left:616px;top:64px">
  <svg class="label__shape" viewBox="0 0 535 665" preserveAspectRatio="none"><use href="#labelOutline" class="label__halo"/><use href="#labelOutline" class="label__body"/></svg>
  <div class="label__heading">Ingredients:</div>
  <p class="label__ingredients">eau, malt, houblon, epices, levure, sucre, fruits</p>
  <div class="label__fact label__fact--net"><span class="label__fact-key">Netto:</span><span class="label__fact-value">330 ml</span></div>
  <div class="label__fact label__fact--maker"><span class="label__fact-key">Brewed by:</span><span class="label__fact-value">Halden</span></div>
</div>

<!-- Red -->
<div class="label label--small label--red label--front" style="left:154px;top:658px">
  <svg class="label__shape" viewBox="0 0 535 665" preserveAspectRatio="none"><use href="#labelOutline" class="label__halo"/><use href="#labelOutline" class="label__body"/></svg>
  <div class="label__mark">HALDEN</div>
  <div class="label__brand">HALDEN</div>
  <div class="label__since">.WINE SINCE 1931</div>
  <div class="label__variety">Red</div>
  <div class="label__rule"></div>
  <div class="label__series">[solstice]</div>
</div>
<div class="label label--small label--red label--back" style="left:352px;top:658px">
  <svg class="label__shape" viewBox="0 0 535 665" preserveAspectRatio="none"><use href="#labelOutline" class="label__halo"/><use href="#labelOutline" class="label__body"/></svg>
  <div class="label__heading">Ingredients:</div>
  <p class="label__ingredients">eau, malt, houblon, epices, levure, sucre, fruits</p>
  <div class="label__fact label__fact--net"><span class="label__fact-key">Netto:</span><span class="label__fact-value">330 ml</span></div>
  <div class="label__fact label__fact--maker"><span class="label__fact-key">Brewed by:</span><span class="label__fact-value">Halden</span></div>
</div>

<!-- Sweet -->
<div class="label label--small label--sweet label--front" style="left:664px;top:658px">
  <svg class="label__shape" viewBox="0 0 535 665" preserveAspectRatio="none"><use href="#labelOutline" class="label__halo"/><use href="#labelOutline" class="label__body"/></svg>
  <div class="label__mark">HALDEN</div>
  <div class="label__brand">HALDEN</div>
  <div class="label__since">.WINE SINCE 1931</div>
  <div class="label__variety">Sweet</div>
  <div class="label__rule"></div>
  <div class="label__series">[solstice]</div>
</div>
<div class="label label--small label--sweet label--back" style="left:862px;top:658px">
  <svg class="label__shape" viewBox="0 0 535 665" preserveAspectRatio="none"><use href="#labelOutline" class="label__halo"/><use href="#labelOutline" class="label__body"/></svg>
  <div class="label__heading">Ingredients:</div>
  <p class="label__ingredients">eau, malt, houblon, epices, levure, sucre, fruits</p>
  <div class="label__fact label__fact--net"><span class="label__fact-key">Netto:</span><span class="label__fact-value">330 ml</span></div>
  <div class="label__fact label__fact--maker"><span class="label__fact-key">Brewed by:</span><span class="label__fact-value">Halden</span></div>
</div>

<!-- Top wine -->
<div class="label label--small label--top label--front" style="left:154px;top:928px">
  <svg class="label__shape" viewBox="0 0 535 665" preserveAspectRatio="none"><use href="#labelOutline" class="label__halo"/><use href="#labelOutline" class="label__body"/></svg>
  <div class="label__mark">HALDEN</div>
  <div class="label__brand">HALDEN</div>
  <div class="label__since">.WINE SINCE 1931</div>
  <div class="label__variety label__variety--long">Top Wine Category</div>
  <div class="label__rule"></div>
  <div class="label__series">[solstice]</div>
</div>
<div class="label label--small label--top label--back" style="left:352px;top:928px">
  <svg class="label__shape" viewBox="0 0 535 665" preserveAspectRatio="none"><use href="#labelOutline" class="label__halo"/><use href="#labelOutline" class="label__body"/></svg>
  <div class="label__heading">Ingredients:</div>
  <p class="label__ingredients">eau, malt, houblon, epices, levure, sucre, fruits</p>
  <div class="label__fact label__fact--net"><span class="label__fact-key">Netto:</span><span class="label__fact-value">330 ml</span></div>
  <div class="label__fact label__fact--maker"><span class="label__fact-key">Brewed by:</span><span class="label__fact-value">Halden</span></div>
</div>

<!-- Sparkle -->
<div class="label label--small label--sparkle label--front" style="left:664px;top:928px">
  <svg class="label__shape" viewBox="0 0 535 665" preserveAspectRatio="none"><use href="#labelOutline" class="label__halo"/><use href="#labelOutline" class="label__body"/></svg>
  <div class="label__mark">HALDEN</div>
  <div class="label__brand">HALDEN</div>
  <div class="label__since">.WINE SINCE 1931</div>
  <div class="label__variety">Sparkle</div>
  <div class="label__rule"></div>
  <div class="label__series">[solstice]</div>
</div>
<div class="label label--small label--sparkle label--back" style="left:862px;top:928px">
  <svg class="label__shape" viewBox="0 0 535 665" preserveAspectRatio="none"><use href="#labelOutline" class="label__halo"/><use href="#labelOutline" class="label__body"/></svg>
  <div class="label__heading">Ingredients:</div>
  <p class="label__ingredients">eau, malt, houblon, epices, levure, sucre, fruits</p>
  <div class="label__fact label__fact--net"><span class="label__fact-key">Netto:</span><span class="label__fact-value">330 ml</span></div>
  <div class="label__fact label__fact--maker"><span class="label__fact-key">Brewed by:</span><span class="label__fact-value">Halden</span></div>
</div>

</body>
</html>
```